Mirrorglow 90's Revival club night

I am after either an A5 or DL flyer but also the formats for using the design on social media etc.
The flyer is for a 90's revival club night at a nightclub that was well attended in the 90's . A special guest PA - Honey Q famous for her single 'Carry me through the starlight' ,is performing.
I have a logo for the night that may have to be altered / edited to fit in with your design (Colours changed etc) but also have a logo for the artist that may be more restrictive in regards to any changes.Both are attached.
Look forward to hearing from you shortly,

Tam

Reason: Required text to go on the flyer has now be added to the brief. Majority of designs submitted didn't seem to reflect to '90's nightclub' feel we were hoping for. Most of the designs used the colour scheme based on the 'Mirrorglow' logo. We are hoping that these colours can be ignored with some designs and that the logo is made of of different colours that would make it easier for it to fit in with the designers ideas. Regards Tam

Target Market(s)

20 to 50 years age range who use to go clubbing / still do / love the 90's music. Club that they use to attend in the 90's is where the event is being held

Industry/Entity Type

Club

Requirements
Must have
• Both the logos for the event ( Mirrorglow 90's Revival and Honey Q ) must be included on the flyer. Colours and the format can be altered on the mirrorglow logo but the design should remain as close to the original as sent. 90's font and images would also be a must if possible. Honey Q logo can have colors altered, but not the font or design.
• Text required as follows :
• Venue : Club Orbit, Pellingford Lane, Westbury, Wiltshire
• Date : Saturday 10th June 2017
• Time : 8.30pm till 3am
• Very special guest PA ‘ HONEY Q’ ‘Carry me through the starlight’
• DJ’s : Main room – Danny Holtsby ( Arcade 77 / Mirrorglow )
• Room 2 – Simon P
• Full club décor with Laser lightshow, CO’2 cannons and pryrotechnics
• Tickets : £15 VIP / £10 General Admission – Available from : https://www.passgate-example.co.uk/venue/QZTRWN
• Or ‘Club Orbit’ : 01632 960418
• Web : www.ravebackclub-example.co.uk
Nice to have
• open to ideas
Should not have
• Not to cheesy ........

```html
<!DOCTYPE html>
<html lang="en">
<head>
<meta charset="utf-8">
<title>Mirrorglow 90's Revival – Club Orbit</title>
<link rel="stylesheet" href="https://fonts.googleapis.com/css2?family=Cinzel:wght@700&family=Cookie&family=Oswald:wght@500;700&family=Russo+One&display=swap">
<style>
  :root {
    --page-bg: #e9ecef;
    --ice-light: #bfe4f6;
    --ice-mid: #5fb3e0;
    --ice-deep: #2a6fb8;
    --ice-title: #dff4ff;
    --ice-title-edge: #3a88c8;
    --gold: #f0b84a;
    --logo-yellow: #f7e21c;
    --white: #ffffff;
    --navy: #12336e;
    --lip-pink: #d2438f;
    --lip-dark: #8e1f5e;
    --disco-silver: #c9d3dc;
    --disco-bronze: #a87a58;
  }
  * { box-sizing: border-box; margin: 0; padding: 0; }
  html, body { width: 1200px; height: 900px; overflow: hidden; background: var(--page-bg); }

  .flyer {
    position: absolute;
    left: 315px; top: 20px;
    width: 570px; height: 860px;
    overflow: hidden;
    background:
      radial-gradient(ellipse at 30% 20%, rgba(255,255,255,.55), transparent 55%),
      radial-gradient(ellipse at 80% 80%, rgba(255,255,255,.35), transparent 50%),
      linear-gradient(160deg, var(--ice-light) 0%, var(--ice-mid) 45%, var(--ice-deep) 100%);
    box-shadow: 0 6px 24px rgba(0,0,0,.25);
    font-family: "Oswald", sans-serif;
    color: var(--white);
  }

  .event-logo {
    position: absolute; left: 28px; top: 82px;
    display: flex; align-items: center; gap: 12px;
    font-family: "Russo One", sans-serif;
    color: var(--logo-yellow);
    font-size: 32px; line-height: 1;
  }
  .event-logo .mark { width: 22px; height: 22px; background: var(--logo-yellow); }
  .event-logo small { display: block; font-size: 20px; margin-top: 6px; }

  .event-info { position: absolute; right: 22px; top: 26px; text-align: right; }
  .event-day { font-family: "Cookie", cursive; font-size: 50px; line-height: .9; }
  .event-date { font-family: "Russo One", sans-serif; font-size: 19px; margin-top: 2px; }
  .event-address { font-family: "Russo One", sans-serif; font-size: 20px; color: var(--gold); line-height: 1.2; margin-top: 10px; }
  .event-time { font-family: "Cookie", cursive; font-size: 28px; margin-top: 2px; }

  .scene-art {
    position: absolute; left: 35px; top: 170px; width: 500px; height: 340px;
    border-radius: 50%;
    background: radial-gradient(ellipse at 50% 40%, var(--disco-silver) 0%, var(--disco-bronze) 45%, rgba(40,50,70,.55) 75%, transparent 100%);
  }
  .lips-art {
    position: absolute; left: 55px; top: 520px; width: 460px; height: 240px;
    border-radius: 50%;
    background: radial-gradient(ellipse at 50% 45%, var(--lip-pink) 0%, var(--lip-dark) 70%, transparent 100%);
  }

  .club-title {
    position: absolute; left: 0; right: 0; top: 222px;
    text-align: center;
    font-family: "Cinzel", serif; font-weight: 700;
    font-size: 112px; line-height: .98;
    color: var(--ice-title);
    -webkit-text-stroke: 2px var(--ice-title-edge);
    text-shadow: 0 4px 10px rgba(0,40,90,.45);
  }

  .guest-line {
    position: absolute; left: 0; right: 0; top: 490px;
    text-align: center; white-space: nowrap;
    font-family: "Oswald", sans-serif; font-weight: 700;
    font-size: 17px; letter-spacing: .2px;
    color: var(--white);
    text-shadow: 0 0 4px var(--navy), 0 0 2px var(--navy);
  }

  .artist-logo {
    position: absolute; left: 0; right: 0; top: 548px;
    text-align: center; font-family: "Russo One", sans-serif;
    font-size: 84px; line-height: 1;
    color: var(--white);
  }
  .artist-badge {
    position: absolute; left: 258px; top: 646px;
    width: 54px; height: 20px; background: var(--white); border-radius: 3px;
  }

  .lineup, .tickets {
    position: absolute;
    font-weight: 500; font-size: 14px; line-height: 1.25; letter-spacing: .4px;
    white-space: nowrap;
    text-shadow: 0 0 3px rgba(18,51,110,.6);
  }
  .lineup { left: 18px; top: 672px; }
  .tickets { right: 24px; top: 742px; text-align: right; }
</style>
</head>
<body>
  <main class="flyer">
    <div class="event-logo">
      <span class="mark"></span>
      <div>Mirrorglow<small>90's Revival</small></div>
    </div>

    <div class="event-info">
      <p class="event-day">Saturday</p>
      <p class="event-date">10TH JUNE 2017</p>
      <p class="event-address">PELLINGFORD LANE,<br>WESTBURY, WILTSHIRE</p>
      <p class="event-time">8.30pm till 3am</p>
    </div>

    <div class="scene-art" role="img" aria-label="Mirror disco ball flanked by retro microphones and vinyl records"></div>
    <div class="lips-art" role="img" aria-label="Glossy pink lips"></div>

    <h1 class="club-title">CLUB<br>ORBIT</h1>

    <p class="guest-line">VERY SPECIAL GUEST PA ‘ HONEY Q’ ‘CARRY ME THROUGH THE STARLIGHT’</p>

    <p class="artist-logo">Honey Q</p>
    <span class="artist-badge"></span>

    <div class="lineup">
      <p>DJS : MAIN ROOM – DANNY HOLTSBY ( ARCADE 77 / MIRRORGLOW )</p>
      <p>ROOM 2 – SIMON P</p>
      <p>FULL CLUB DÉCOR WITH LASER LIGHTSHOW,</p>
      <p>CO'2 CANNONS AND PRYROTECHNICS</p>
    </div>

    <div class="tickets">
      <p>TICKETS : £15 VIP / £10 GENERAL ADMISSION</p>
      <p>AVAILABLE FROM : HTTPS://WWW.PASSGATE-EXAMPLE.CO.UK/VENUE/QZTRWN</p>
      <p>OR ‘CLUB ORBIT’ : 01632 960418</p>
      <p>WEB : WWW.RAVEBACKCLUB-EXAMPLE.CO.UK</p>
    </div>
  </main>
</body>
</html>
```